New Business Card

Use website for color, logo and theme.

http://www.plumwickonline.com/

Back side of card should be programs listed on home page of website

1) Phone Number is (800) 555-0142 x23
2) Fax (240) 555-0187
3) Address is - 647 W Harlowe Street, Suite 312, Baltimore, MD 21201
4) NMLS #738516

```html
<!DOCTYPE html>
<html lang="en">
<head>
<meta charset="utf-8">
<title>Plumwick Financial Services – Business Card</title>
<link rel="stylesheet" href="https://fonts.googleapis.com/css2?family=Lato:wght@400;700&display=swap">
<style>
  :root {
    --bg: #e4e4e4;
    --card: #ffffff;
    --blue: #1a4f8f;
    --blue-deep: #104c8c;
    --gold: #9c8a3c;
    --ink: #1b1b1b;
    --photo-dark: #2a2a2a;
    --photo-light: #8a7a70;
  }
  * { box-sizing: border-box; margin: 0; padding: 0; }
  html, body { width: 1200px; height: 720px; overflow: hidden; }
  body {
    background: var(--bg);
    font-family: "Lato", sans-serif;
    color: var(--ink);
    position: relative;
  }
  .card {
    position: absolute;
    top: 206px;
    width: 540px;
    height: 308px;
    background: var(--card);
    border-radius: 8px;
    overflow: hidden;
  }
  .card-front { left: 40px; }
  .card-back { left: 620px; }

  /* Front */
  .holder-name {
    position: absolute; left: 24px; top: 22px;
    font-size: 24px; font-weight: 700; color: var(--blue);
  }
  .holder-title { position: absolute; left: 24px; top: 55px; font-size: 15px; }
  .contact-list {
    position: absolute; left: 24px; top: 88px;
    list-style: none; font-size: 15px; line-height: 18.5px;
  }
  .contact-list li { display: flex; align-items: center; gap: 6px; }
  .contact-list svg { width: 14px; height: 12px; fill: var(--blue); flex: none; }
  .address { position: absolute; left: 24px; top: 168px; font-size: 15px; line-height: 18.5px; }
  .portrait {
    position: absolute; left: 290px; top: 22px; width: 250px; height: 286px;
    background: radial-gradient(ellipse at 48% 30%, var(--photo-light) 0 22%, transparent 23%),
                linear-gradient(180deg, #ffffff 0 35%, var(--photo-dark) 60%);
  }
  .front-band { position: absolute; left: 0; top: 0; width: 540px; height: 308px; }
  .nmls {
    position: absolute; left: 26px; top: 247px;
    font-size: 15px; color: #ffffff; letter-spacing: 0.3px;
  }
  .badges { position: absolute; left: 26px; top: 272px; display: flex; gap: 10px; align-items: center; }
  .badge { background: #ffffff; opacity: 0.9; }
  .badge-sq { width: 20px; height: 26px; border-radius: 2px; }
  .badge-sq-wide { width: 30px; height: 26px; border-radius: 2px; background: #2c66b0; border: 1px solid #ffffff; }
  .badge-wide { width: 126px; height: 22px; border-radius: 2px; }

  /* Back */
  .brand {
    position: absolute; left: 0; right: 0; top: 30px;
    display: flex; align-items: center; justify-content: center; gap: 10px;
  }
  .brand-dot { width: 44px; height: 44px; border-radius: 50%; background: var(--gold); }
  .brand-name { font-size: 17px; font-weight: 700; color: var(--blue); }
  .programs { position: absolute; left: 0; right: 0; top: 118px; text-align: center; }
  .program-group + .program-group { margin-top: 11px; }
  .program-heading { font-size: 15px; font-weight: 700; line-height: 17px; }
  .program-row {
    display: flex; justify-content: center; gap: 10px;
    font-size: 12.5px; line-height: 16px; list-style: none;
  }
  .program-row li { display: flex; align-items: center; gap: 3px; white-space: nowrap; }
  .program-row svg { width: 14px; height: 13px; flex: none; }
  .tick-box { fill: none; stroke: var(--blue); stroke-width: 1.4; }
  .tick-mark { fill: none; stroke: var(--blue); stroke-width: 2.4; stroke-linecap: round; stroke-linejoin: round; }
  .back-rule { position: absolute; left: 0; right: 0; top: 288px; height: 2px; background: var(--gold); }
  .back-band { position: absolute; left: 0; right: 0; top: 290px; bottom: 0; background: var(--blue-deep); }
</style>
</head>
<body>
<svg width="0" height="0" style="position:absolute">
  <defs>
    <symbol id="tick" viewBox="0 0 14 13">
      <rect class="tick-box" x="1" y="3" width="9" height="9"/>
      <path class="tick-mark" d="M3 7 L6 10 L13 1"/>
    </symbol>
  </defs>
</svg>

<section class="card card-front">
  <div class="portrait" role="img" aria-label="Portrait photo of the owner in a dark suit"></div>
  <svg class="front-band" viewBox="0 0 540 308" aria-hidden="true">
    <path d="M0 222 C150 214 330 232 500 308 L540 308 L540 308 L0 308 Z" fill="#9c8a3c"/>
    <path d="M0 228 C150 224 300 250 430 308 L0 308 Z" fill="#104c8c"/>
  </svg>
  <h1 class="holder-name">Marcus Bellamy</h1>
  <p class="holder-title">Owner</p>
  <ul class="contact-list">
    <li><svg viewBox="0 0 14 12"><path d="M1 4 Q7 -1 13 4 L11 5.5 L9.5 3.8 L4.5 3.8 L3 5.5 Z M3 6 H11 V11 H3 Z"/></svg><span>&nbsp;(800) 555-0142 x23</span></li>
    <li><svg viewBox="0 0 14 12"><path d="M4 0 H10 V3 H4 Z M1 4 H13 V9 H11 V7 H3 V9 H1 Z M3 8 H11 V12 H3 Z"/></svg><span>(240) 555-0187</span></li>
    <li><svg viewBox="0 0 14 12"><path d="M0 1 H14 V11 H0 Z M1.5 2.5 L7 7 L12.5 2.5 V9.5 H1.5 Z" fill-rule="evenodd"/></svg><span>info@plumwickonline.com</span></li>
    <li><svg viewBox="0 0 14 12"><path d="M1 0 H13 V8 H1 Z M2.5 1.5 V6.5 H11.5 V1.5 Z M5 9 H9 V10 H11 V12 H3 V10 H5 Z" fill-rule="evenodd"/></svg><span>www.plumwickonline.com</span></li>
  </ul>
  <p class="address">647 W Harlowe Street<br>Suite 312, Baltimore, MD 21201</p>
  <p class="nmls">NMLS #738516</p>
  <div class="badges">
    <span class="badge badge-sq"></span>
    <span class="badge-sq-wide"></span>
    <span class="badge badge-sq"></span>
    <span class="badge badge-wide"></span>
  </div>
</section>

<section class="card card-back">
  <div class="brand">
    <span class="brand-dot"></span>
    <span class="brand-name">Plumwick Financial Services, Inc.</span>
  </div>
  <div class="programs">
    <div class="program-group">
      <h2 class="program-heading">Traditional Loan Programs</h2>
      <ul class="program-row">
        <li><svg><use href="#tick"/></svg>FHA loans starting at 580 score</li>
        <li><svg><use href="#tick"/></svg>FHA 203k starting at 600 score</li>
      </ul>
      <ul class="program-row">
        <li><svg><use href="#tick"/></svg>VA starting at 600 score (100% LTV)</li>
        <li><svg><use href="#tick"/></svg>All Conventional loan programs.</li>
      </ul>
    </div>
    <div class="program-group">
      <h2 class="program-heading">Low Credit Score Programs</h2>
      <ul class="program-row">
        <li><svg><use href="#tick"/></svg>500 score up to 70% LTV</li>
        <li><svg><use href="#tick"/></svg>540 score up to 75% LTV</li>
        <li><svg><use href="#tick"/></svg>580 score up to 96.5% LTV</li>
      </ul>
    </div>
    <div class="program-group">
      <h2 class="program-heading">Alternative Loan Programs</h2>
      <ul class="program-row">
        <li><svg><use href="#tick"/></svg>Investor Fix &amp; Flip Rehab Loans</li>
        <li><svg><use href="#tick"/></svg>Investor Stated Loans</li>
      </ul>
      <ul class="program-row">
        <li><svg><use href="#tick"/></svg>Foreign National Loans</li>
        <li><svg><use href="#tick"/></svg>Limited Documentation Loans (1 year tax or W2)</li>
      </ul>
    </div>
  </div>
  <div class="back-rule"></div>
  <div class="back-band"></div>
</section>
</body>
</html>
```